IT Services

We come to you
Only $49/hr
No contract, no monthly fee
Software engineer on staff
remote assistance or visit in your office

On the back of the card I want to list services.

- Server setup
- Network troubleshooting
- Printer setup
- Secure backup setup
- Software installation
- Wireless network setup
- Wired network setup
- Disaster recovery
- Website management
- Any other technology related support
- Email setup
- HIPAA compliance review and setup
Updates

the URL is: GEARFIXPRO.ZONE please use it on the card

On the card we need to mention "Connect remotely to address your IT issues" if there is enough room as well as "we go to you"

Industry/Entity Type

Printer

Contact Information for Business Card

I want a busoiness card to offer my services to doctor offices, it can be dentists, Otamatry, and other professions. I provide the following service. My plan is to go to their office and drop off my card. I don't want them to forget about it that is why I am paying for the design. I like hand writing design formats.

```html
<!DOCTYPE html>
<html lang="en">
<head>
<meta charset="utf-8">
<title>gearfixpro.zone business card</title>
<link rel="stylesheet" href="https://fonts.googleapis.com/css2?family=Arimo:wght@400;700&display=swap">
<style>
  :root {
    --green: #077a3c;
    --blue: #3a77c4;
    --yellow: #f4ec1c;
    --white: #ffffff;
    --paper-light: #f7f7f7;
    --paper-shade: #d4d4d4;
    --ink: #1a1a1a;
  }
  html, body {
    margin: 0;
    padding: 0;
    width: 1200px;
    height: 353px;
    overflow: hidden;
    background: var(--white);
    font-family: "Arimo", Arial, Helvetica, sans-serif;
  }
  .canvas {
    position: relative;
    width: 1200px;
    height: 353px;
  }
  .card-front {
    position: absolute;
    left: 0; top: 0;
    width: 595px; height: 353px;
    background: var(--green);
    overflow: hidden;
  }
  .card-back {
    position: absolute;
    left: 595px; top: 0;
    width: 605px; height: 353px;
    background: var(--white);
  }
  .bar { position: absolute; }
  .bar--white  { background: var(--white); }
  .bar--green  { background: var(--green); }
  .bar--blue   { background: var(--blue); }
  .bar--yellow { background: var(--yellow); }

  .code-page {
    position: absolute;
    left: 0; top: 0;
    width: 142px;
    height: 128px;
    background: linear-gradient(135deg, var(--paper-light) 0%, var(--paper-light) 55%, var(--paper-shade) 100%);
    clip-path: polygon(0 0, 100% 0, 100% 58%, 72% 100%, 0 100%);
  }
  .site-name {
    position: absolute;
    margin: 0;
    font-weight: 700;
    font-size: 58px;
    letter-spacing: -0.5px;
    line-height: 1;
    white-space: nowrap;
  }
  .card-front .site-name {
    right: 10px;
    top: 124px;
    color: var(--white);
  }
  .card-back .site-name {
    left: 40px; right: 0;
    text-align: center;
    top: 124px;
    color: var(--green);
  }
  .offer {
    position: absolute;
    left: 13px;
    top: 224px;
    margin: 0;
    padding: 0;
    list-style: none;
    color: var(--white);
    font-weight: 700;
    font-size: 20px;
    line-height: 25px;
  }
  .contact {
    position: absolute;
    right: 12px;
    top: 255px;
    text-align: right;
    color: var(--white);
    font-weight: 700;
  }
  .contact__name {
    font-size: 34px;
    line-height: 38px;
  }
  .contact__phone {
    font-size: 26px;
    line-height: 30px;
  }
  .services {
    position: absolute;
    left: 36px; right: 0;
    top: 189px;
    margin: 0;
    padding: 0;
    text-align: center;
    color: var(--ink);
    font-size: 17.8px;
    line-height: 21.6px;
  }
  .services__row { display: block; white-space: nowrap; }
  .services__item::before {
    content: "";
    display: inline-block;
    width: 7px; height: 7px;
    border-radius: 50%;
    background: var(--green);
    margin: 0 4px 2px 3px;
    vertical-align: middle;
  }
</style>
</head>
<body>
<main class="canvas">
  <section class="card-front" aria-label="Card front">
    <div class="code-page" role="img" aria-label="Page of program code with a turned-up corner"></div>

    <div class="bar bar--white"  style="left:251px; top:34px; width:344px; height:11px;"></div>
    <div class="bar bar--blue"   style="left:148px; top:49px; width:447px; height:11px;"></div>
    <div class="bar bar--yellow" style="left:302px; top:67px; width:293px; height:10px;"></div>

    <h1 class="site-name">gearfixpro.zone</h1>

    <ul class="offer">
      <li>Only $49/hr.</li>
      <li>No contract.</li>
      <li>No monthly fee.</li>
      <li>We come to you.</li>
    </ul>

    <div class="contact">
      <div class="contact__name">Dara Vollen</div>
      <div class="contact__phone">1.800.555.0148</div>
    </div>
  </section>

  <section class="card-back" aria-label="Card back">
    <div class="bar bar--green"  style="left:27px; top:34px; width:427px; height:11px;"></div>
    <div class="bar bar--blue"   style="left:27px; top:49px; width:556px; height:11px;"></div>
    <div class="bar bar--yellow" style="left:27px; top:66px; width:363px; height:10px;"></div>

    <h2 class="site-name">gearfixpro.zone</h2>

    <p class="services">
      <span class="services__row"><span class="services__item">Server setup</span> <span class="services__item">Network troubleshooting</span> <span class="services__item">Printer setup</span></span>
      <span class="services__row"><span class="services__item">Secure backup setup</span> <span class="services__item">Software installation</span> <span class="services__item">Wireless network setup</span></span>
      <span class="services__row"><span class="services__item">Wired network setup</span> <span class="services__item">Disaster recovery</span> <span class="services__item">Website management</span></span>
      <span class="services__row"><span class="services__item">Any other technology related support</span> <span class="services__item">Email setup</span></span>
      <span class="services__row"><span class="services__item">HIPAA compliance review and setup</span></span>
    </p>
  </section>
</main>
</body>
</html>
```